LumoQuest.com (Escape Room) WordPress Website Redesign

Our company name is Lumo Quest. We are an escape room in San Marcos Texas. We need a complete website redesign with bookeo booking software integrated.

Our current site is lumoquest.com. We need a more user friendly and mobile friendly site. Our current site shows 2 rooms but we are adding 2 more next month and removing one.

I really like the designs of

brindlepuzzlehall.com/

Target Market(s)

Women 21-39

Industry/Entity Type

Entertainment

Coding

Coded - Design and coding required

Number of Pages Required

1 page

Font styles to use
Serif
Sans Serif

Requirements
Must have
• Bookeo booking intergrated. mobile and full verison
Nice to have
• clean design, wordpress, easy to access backend

```html
<!DOCTYPE html>
<html lang="en">
<head>
<meta charset="utf-8">
<title>Lumo Quest — Escape Room San Marcos</title>
<link rel="stylesheet" href="https://fonts.googleapis.com/css2?family=Lato:ital,wght@0,400;0,700;0,900;1,400&family=Montserrat:wght@600;700;800&display=swap">
<style>
:root{
  --orange:#f39200;
  --orange-soft:#f6a21c;
  --ink:#161616;
  --dark:#262626;
  --darker:#1a1a1a;
  --grey-bg:#ececec;
  --light-bg:#f7f7f7;
  --text:#333;
  --muted:#8a8a8a;
  --line:#d4d4d4;
  --white:#fff;
}
*{box-sizing:border-box;margin:0;padding:0}
html,body{width:1200px;height:2384px;overflow:hidden}
body{font-family:"Lato",Arial,sans-serif;color:var(--text);background:var(--white);position:relative}
.abs{position:absolute}
.brand{display:flex;align-items:center;gap:10px;font-family:"Montserrat",Arial,sans-serif;font-weight:800;color:var(--orange);letter-spacing:1px;text-transform:uppercase}
.brand .dot{border-radius:50%;background:var(--orange);display:block}

/* header */
.site-header{top:0;left:0;width:1200px;height:98px;background:linear-gradient(#fff,#f1f1f1);border-top:3px solid #bdbdbd}
.site-header .brand{position:absolute;left:164px;top:29px;font-size:34px}
.site-header .brand .dot{width:34px;height:34px}
.header-phone{position:absolute;right:162px;top:12px;display:flex;align-items:center;gap:10px;font-weight:700;font-size:17px;color:#222}
.main-nav{position:absolute;left:577px;top:50px;display:flex;gap:0}
.main-nav a{font-family:"Montserrat",Arial,sans-serif;font-weight:700;font-size:15px;color:var(--ink);text-decoration:none;padding:6px 8px;margin-right:18px}
.main-nav a.active{background:var(--ink);color:#fff;outline:2px solid #fff;box-shadow:0 0 0 3px var(--ink)}

/* hero */
.hero{top:98px;left:0;width:1200px;height:530px;background:radial-gradient(ellipse at 50% 38%,#4a4a4a 0%,#262626 45%,#0c0c0c 100%)}
.hero h1{position:absolute;top:246px;width:100%;text-align:center;font-family:"Montserrat",Arial,sans-serif;font-weight:700;font-size:38px;color:#fff;letter-spacing:.5px}
.hero h1 span{color:var(--orange);font-size:44px}
.slider-dots{position:absolute;top:496px;left:565px;display:flex;gap:7px}
.slider-dots i{width:12px;height:12px;border:1.5px solid #ddd;border-radius:50%;display:block}
.slider-dots i.on{border-color:var(--orange)}

/* about */
.about{top:628px;left:0;width:1200px;height:238px;background:var(--light-bg)}
.about h2{position:absolute;top:50px;width:100%;display:flex;justify-content:center;align-items:center;gap:14px;font-family:"Montserrat",Arial,sans-serif;font-weight:700;font-size:28px;color:var(--ink)}
.about h2 .brand{font-size:32px}
.about h2 .brand .dot{width:30px;height:30px}
.about p{position:absolute;left:178px;top:124px;width:844px;text-align:center;font-size:13.5px;line-height:21px;color:#444}

/* rooms */
.rooms{top:866px;left:0;width:1200px;height:381px}
.room{position:absolute;top:0;width:600px;height:381px;color:#fff;text-align:center}
.room-left{left:0;background:linear-gradient(135deg,#2b2b2b,#161616 60%,#222)}
.room-right{left:600px;background:linear-gradient(135deg,#f6a21c,#e68a00 60%,#c97400)}
.room h3{position:absolute;top:78px;width:100%;font-family:"Montserrat",Arial,sans-serif;font-weight:700;font-size:29px;line-height:37px;letter-spacing:.5px}
.room-left h3{left:-20px}
.room-right h3{left:-10px}
.room p{position:absolute;top:168px;font-size:13.5px;line-height:22px}
.room-left p{left:156px;width:324px}
.room-right p{left:110px;width:330px}
.book-btn{position:absolute;top:254px;width:181px;height:36px;background:var(--ink);border:2px solid var(--orange);display:flex;align-items:center;font-family:"Montserrat",Arial,sans-serif;font-weight:700;font-size:15px;color:#fff;padding-left:13px}
.room-left .book-btn{left:229px}
.room-right .book-btn{left:180px;border-color:var(--ink)}
.book-btn .arrow{position:absolute;right:8px;top:-5px;width:42px;height:42px;border-radius:50%;background:var(--ink);border:2px solid var(--orange);display:flex;align-items:center;justify-content:center}
.room-badge{position:absolute;left:548px;top:134px;width:104px;height:104px;border-radius:50%;background:#fff;border:5px solid var(--ink);box-shadow:0 0 0 4px var(--orange)}
.room-badge::after{content:"";position:absolute;left:24px;top:24px;width:46px;height:46px;border-radius:50%;background:var(--orange)}

/* who should play */
.who{top:1247px;left:0;width:1200px;height:464px;background:var(--grey-bg)}
.section-title{position:absolute;width:100%;text-align:center;font-family:"Montserrat",Arial,sans-serif;font-weight:700;font-size:27px;color:var(--ink)}
.section-title span{color:var(--orange)}
.divider{position:absolute;left:400px;width:400px;height:20px}
.who .section-title{top:46px}
.who .divider{top:83px}
.audience{position:absolute;top:126px;width:200px;text-align:center}
.audience .icon{width:112px;height:112px;margin:0 auto;border-radius:50%;background:#e2dfd9;border:5px solid #d6d2ca;display:flex;align-items:center;justify-content:center}
.audience .icon span{width:74px;height:74px;border-radius:50%;background:#f5f3ef;display:flex;align-items:center;justify-content:center}
.audience h4{margin-top:20px;font-family:"Montserrat",Arial,sans-serif;font-weight:700;font-size:16px;line-height:21px;color:var(--ink)}
.audience p{margin:14px auto 0;width:190px;font-size:12.5px;line-height:19px;color:#333}

/* testimonials */
.testimonials{top:1711px;left:0;width:1200px;height:300px;background:#fff}
.testimonials .section-title{top:36px}
.testimonials .divider{top:76px}
.quote-card{position:absolute;top:128px;width:414px;height:130px}
.quote-card .avatar{position:absolute;left:0;top:0;width:92px;height:92px;border-radius:50%;border:4px solid var(--orange);background:linear-gradient(#c9d3da,#8f9ba4)}
.quote-card .avatar::after{content:"";position:absolute;right:-10px;bottom:6px;border-left:14px solid var(--orange);border-top:8px solid transparent;border-bottom:8px solid transparent;transform:rotate(35deg)}
.quote-card blockquote{position:absolute;left:116px;top:12px;width:290px;font-style:italic;font-size:11.5px;line-height:20px;color:#444}
.quote-card .qmark{position:absolute;left:116px;top:8px;font-family:Georgia,serif;font-size:44px;line-height:30px;color:#cfcfcf}
.quote-card blockquote{text-indent:34px}
.quote-card .rule{position:absolute;left:0;top:114px;width:414px;height:2px;background:linear-gradient(90deg,transparent,#d9d9d9 15%,#d9d9d9 85%,transparent)}
.quote-card cite{position:absolute;top:128px;left:140px;font-style:normal;font-family:"Montserrat",Arial,sans-serif;font-weight:700;font-size:12px;color:var(--ink)}
.t-dots{position:absolute;left:998px;top:282px;display:flex;gap:4px}
.t-dots i{width:8px;height:8px;border-radius:50%;background:#ccc;display:block}
.t-dots i.on{background:var(--orange)}

/* footer */
.wave{top:2000px;left:0;width:1200px;height:110px}
.site-footer{top:2090px;left:0;width:1200px;height:255px;background:var(--dark);color:#ddd}
.foot-col{position:absolute;top:40px}
.foot-col h5{font-family:"Montserrat",Arial,sans-serif;font-weight:700;font-size:13.5px;color:#fff;letter-spacing:.4px;margin-bottom:22px}
.quick-links{left:164px;width:110px}
.quick-links li{list-style:none;font-size:12px;color:#ddd;padding:8px 0 9px;border-bottom:1px solid #3a3a3a}
.quick-links li:first-child{padding-top:0}
.contact-col{left:343px;width:150px}
.contact-col .row{display:flex;gap:14px;font-size:12px;line-height:16px;padding:0 0 16px;margin-bottom:16px;border-bottom:1px solid #3a3a3a}
.inquiry{left:575px;width:250px}
.inquiry .field{height:28px;background:#3c3c3c;margin-bottom:6px;font-size:11.5px;color:#ddd;padding:7px 10px}
.inquiry .field.msg{height:48px}
.submit-btn{margin-top:20px;width:112px;height:28px;border:1.5px solid var(--orange);background:var(--darker);display:flex;align-items:center;font-family:"Montserrat",Arial,sans-serif;font-weight:700;font-size:12px;color:#fff;padding-left:12px;position:relative}
.submit-btn .arrow{position:absolute;right:4px;top:-3px;width:32px;height:32px;border-radius:50%;border:1.5px solid var(--orange);background:var(--darker);display:flex;align-items:center;justify-content:center}
.hours{left:898px;width:150px}
.hours table{border-collapse:collapse;font-size:12px;line-height:16px}
.hours td{padding:0}
.hours td:last-child{color:var(--orange);padding-left:10px}
.hours .brand{margin-top:16px;font-size:17px}
.hours .brand .dot{width:18px;height:18px}
.vsep{position:absolute;top:40px;width:1px;height:180px;background:#353535}
.bottom-bar{top:2345px;left:0;width:1200px;height:39px;background:var(--darker)}
.bottom-bar p{position:absolute;left:164px;top:13px;font-family:"Montserrat",Arial,sans-serif;font-weight:600;font-size:10.5px;color:#fff;letter-spacing:.3px}
.social{position:absolute;left:946px;top:7px;display:flex;gap:9px}
.social i{width:25px;height:25px;border-radius:50%;background:#1a7fc1;display:block}
</style>
</head>
<body>

<header class="site-header abs">
  <div class="brand">LumoQuest<span class="dot"></span></div>
  <div class="header-phone">
    <svg width="18" height="18" viewBox="0 0 24 24"><path fill="#f39200" d="M6.6 10.8a15 15 0 0 0 6.6 6.6l2.2-2.2c.3-.3.7-.4 1-.2 1.1.4 2.3.6 3.6.6.6 0 1 .4 1 1V20c0 .6-.4 1-1 1A17 17 0 0 1 3 4c0-.6.4-1 1-1h3.5c.6 0 1 .4 1 1 0 1.3.2 2.5.6 3.6.1.3 0 .7-.2 1z"/></svg>
    555-014-2290
  </div>
  <nav class="main-nav">
    <a class="active">HOME</a><a>WHO SHOULD PLAY</a><a>OUR ROOMS</a><a>CONTACT</a>
  </nav>
</header>

<section class="hero abs" role="img" aria-label="Dark stone labyrinth seen from above">
  <h1>PLAN YOUR <span>ESCAPE ROOM</span> ADVENTURE</h1>
  <div class="slider-dots"><i></i><i class="on"></i><i></i><i></i></div>
</section>

<section class="about abs">
  <h2>ABOUT <span class="brand">LumoQuest<span class="dot"></span></span></h2>
  <p>Lorem ipsum dolor sit amet, consectetuer adipiscing elit, sed diam nonummy nibh euismod tincidunt ut laoreet dolore magna aliquam erat volutpat. Ut wisi enim ad minim veniam, quis nostrud exerci tation ullamcorper suscipit lobortis nisl ut aliquip ex ea commodo consequat. Duis autem vel eum iriure dolor in hendrerit in sit vulputate velit esse molestie consequat, vel illum dolore eu feugiat nulla facilisis at vero eros et accumsan et iusto odio dignissim qui blandit praesent luptatum..</p>
</section>

<section class="rooms abs">
  <article class="room room-left" role="img" aria-label="Wall of old padlocks and keys in dark tones">
    <h3>SAN MARCOS<br>ESCAPE ROOM</h3>
    <p>Bob likes to play with chainsaws. Lured into his trap, you now find yourself in a locked room. Luckily his chainsaw has broken down and he has to run...</p>
    <div class="book-btn">BOOK NOW<span class="arrow"><svg width="14" height="12" viewBox="0 0 14 12"><path d="M1 1l5 5-5 5M7 1l5 5-5 5" stroke="#fff" stroke-width="2" fill="none"/></svg></span></div>
  </article>
  <article class="room room-right" role="img" aria-label="Orange-tinted room with digital timer, lamp and side table">
    <h3>AMNESIA<br>ROOM</h3>
    <p>You ate that cafeteria sandwich someone gave you with out hesitation. Unfortunately, they must have put something in it. Now you're locked in a...</p>
    <div class="book-btn">BOOK NOW<span class="arrow"><svg width="14" height="12" viewBox="0 0 14 12"><path d="M1 1l5 5-5 5M7 1l5 5-5 5" stroke="#fff" stroke-width="2" fill="none"/></svg></span></div>
  </article>
  <div class="room-badge"></div>
</section>

<section class="who abs">
  <h2 class="section-title">WHO SHOULD <span>PLAY</span></h2>
  <svg class="divider" viewBox="0 0 400 20"><line x1="0" y1="10" x2="185" y2="10" stroke="#ccc"/><line x1="215" y1="10" x2="400" y2="10" stroke="#ccc"/><circle cx="200" cy="10" r="8" fill="none" stroke="#f39200" stroke-width="2"/><circle cx="200" cy="10" r="4" fill="#f39200"/></svg>

  <div class="audience" style="left:175px">
    <div class="icon"><span><svg width="30" height="24" viewBox="0 0 30 24"><circle cx="11" cy="6" r="5" fill="#222"/><circle cx="21" cy="7" r="4" fill="#222"/><path d="M2 22c0-6 4-9 9-9s9 3 9 9z M19 13c4 0 9 2 9 8h-7c0-3-1-6-2-8z" fill="#222"/></svg></span></div>
    <h4>FAMILY +<br>FRIENDS</h4>
    <p>Take a break from the norm and enjoy a unique immersive experience with your friends and family. You'll have to combine skills to solve puzzles and find clues to get out in under 60 minutes.</p>
  </div>
  <div class="audience" style="left:391px">
    <div class="icon"><span><svg width="28" height="28" viewBox="0 0 28 28"><path d="M5 8a11 11 0 1 1-1 9" stroke="#222" stroke-width="2.5" fill="none"/><path d="M2 3v7h7" stroke="#222" stroke-width="2.5" fill="none"/><path d="M14 8v7l4 3" stroke="#222" stroke-width="2.5" fill="none"/></svg></span></div>
    <h4>GAMERS +<br>ENTHUSIAST</h4>
    <p>There is no pause button and no respawning, this is live. You will need to crack codes and solve puzzles to get out. You have 60 minutes, do you have what it takes?</p>
  </div>
  <div class="audience" style="left:607px">
    <div class="icon"><span><svg width="22" height="30" viewBox="0 0 22 30"><path d="M11 2a8 8 0 0 0-5 14c1 1 1.5 2 1.5 4h7c0-2 .5-3 1.5-4A8 8 0 0 0 11 2z" stroke="#222" stroke-width="2.2" fill="none"/><path d="M7.5 23h7M8.5 27h5" stroke="#222" stroke-width="2.2"/></svg></span></div>
    <h4>COMPANIES +<br>EVENTS</h4>
    <p>Team building has never been so successful! Your group will face challenging puzzles and will have to get organized and work together to get out in under 60 minutes</p>
  </div>
  <div class="audience" style="left:822px">
    <div class="icon"><span><svg width="30" height="30" viewBox="0 0 30 30"><circle cx="15" cy="15" r="13" fill="#222"/><path d="M9 7c3 1 4 4 2 6s-1 5 2 6M19 5c-1 3 1 4 3 5s2 4 0 6c-2 1-3 4-2 7" stroke="#f5f3ef" stroke-width="2" fill="none"/></svg></span></div>
    <h4>TOURISTS +<br>VISITORS</h4>
    <p>In town or just passing thru San Marcos? Stop by and enjoy an hour of immersive fun for everyone: friends, family and colleagues.</p>
  </div>
</section>

<section class="testimonials abs">
  <h2 class="section-title">CLIENTS <span>TESTIMONIALS</span></h2>
  <svg class="divider" viewBox="0 0 400 20"><line x1="0" y1="10" x2="185" y2="10" stroke="#ccc"/><line x1="215" y1="10" x2="400" y2="10" stroke="#ccc"/><circle cx="200" cy="10" r="8" fill="none" stroke="#f39200" stroke-width="2"/><circle cx="200" cy="10" r="4" fill="#f39200"/></svg>

  <figure class="quote-card" style="left:159px">
    <div class="avatar" role="img" aria-label="Portrait photo of a smiling customer"></div>
    <span class="qmark">&ldquo;</span>
    <blockquote>Lorem ipsum dolor sit amet, consect uer adipiscing elit, sed diam nonummy nibh euis mod tincidun nt ut laoreetml dolore magna aliquam erat volutpat. Ut wisi enim ad minim veniam, quis nostrud exer.</blockquote>
    <div class="rule"></div>
    <cite>- MR. OWEN CALLOWAY</cite>
  </figure>
  <figure class="quote-card" style="left:623px">
    <div class="avatar" role="img" aria-label="Portrait photo of a customer in a suit"></div>
    <span class="qmark">&ldquo;</span>
    <blockquote>Lorem ipsum dolor sit amet, consect uer adipiscing elit, sed diam nonummy nibh euis mod tincidun nt ut laoreetml dolore magna aliquam erat volutpat. Ut wisi enim ad minim veniam, quis nostrud exer.</blockquote>
    <div class="rule"></div>
    <cite>- MR. FELIX MARROW</cite>
  </figure>
  <div class="t-dots"><i class="on"></i><i></i><i></i></div>
</section>

<svg class="wave abs" viewBox="0 0 1200 110" preserveAspectRatio="none">
  <path d="M0 10 C250 100 650 110 1200 40 L1200 110 L0 110 Z" fill="#262626"/>
  <path d="M0 10 C250 100 650 110 1200 40" stroke="#111" stroke-width="8" fill="none"/>
  <path d="M520 78 C800 70 1000 40 1200 50 L1200 82 C1000 72 800 82 520 78 Z" fill="#f39200"/>
</svg>

<footer class="site-footer abs">
  <div class="foot-col quick-links">
    <h5>QUICK LINKS</h5>
    <ul><li>HOME</li><li>WHO SHOULD PLAY</li><li>OUR ROOMS</li><li>CONTACT</li></ul>
  </div>
  <div class="vsep" style="left:312px"></div>
  <div class="foot-col contact-col">
    <h5>CONTACT DETAILS</h5>
    <div class="row"><svg width="12" height="16" viewBox="0 0 12 16"><path d="M6 0a6 6 0 0 0-6 6c0 4 6 10 6 10s6-6 6-10a6 6 0 0 0-6-6zm0 8.5A2.5 2.5 0 1 1 6 3.5a2.5 2.5 0 0 1 0 5z" fill="#f39200"/></svg><span>48 Larkspur Ave Ste 3<br>San Marcos TX 78600</span></div>
    <div class="row"><svg width="12" height="14" viewBox="0 0 24 24"><path fill="#f39200" d="M6.6 10.8a15 15 0 0 0 6.6 6.6l2.2-2.2c.3-.3.7-.4 1-.2 1.1.4 2.3.6 3.6.6.6 0 1 .4 1 1V20c0 .6-.4 1-1 1A17 17 0 0 1 3 4c0-.6.4-1 1-1h3.5c.6 0 1 .4 1 1 0 1.3.2 2.5.6 3.6.1.3 0 .7-.2 1z"/></svg><span>555-018-4471</span></div>
    <div class="row" style="border:0"><svg width="12" height="14" viewBox="0 0 12 10"><rect x="0" y="1" width="12" height="8" fill="#f39200"/><path d="M0 1l6 5 6-5" stroke="#262626" fill="none"/></svg><span>hello@lumoquest.com</span></div>
  </div>
  <div class="vsep" style="left:540px"></div>
  <div class="foot-col inquiry">
    <h5>QUICK INQUIRY</h5>
    <div class="field">Name</div>
    <div class="field">Email</div>
    <div class="field msg">Message</div>
    <div class="submit-btn">SUBMIT<span class="arrow"><svg width="12" height="10" viewBox="0 0 14 12"><path d="M1 1l5 5-5 5M7 1l5 5-5 5" stroke="#fff" stroke-width="2" fill="none"/></svg></span></div>
  </div>
  <div class="vsep" style="left:862px"></div>
  <div class="foot-col hours">
    <h5>HOURS</h5>
    <table>
      <tr><td>Monday -</td><td>2pm - 8pm</td></tr>
      <tr><td>Tuesday -</td><td>CLOSED</td></tr>
      <tr><td>Wednesday -</td><td>2pm -8pm</td></tr>
      <tr><td>Thursday-</td><td>2pm -8pm</td></tr>
      <tr><td>Friday-</td><td>2pm -8pm</td></tr>
      <tr><td>Saturday-</td><td>2pm -8pm</td></tr>
      <tr><td>Sunday-</td><td>2pm -8pm</td></tr>
    </table>
    <div class="brand">LumoQuest<span class="dot"></span></div>
  </div>
</footer>

<div class="bottom-bar abs">
  <p>COPYRIGHT © 2016 LUMO QUEST. ALL RIGHTS RESERVED.</p>
  <div class="social"><i></i><i></i><i></i></div>
</div>

</body>
</html>
```